Voice of the River CD cover

We need a cover for our new CD of old middle eastern Jewish music which draws the eye. The title of the CD is Kol Nahar Yafi which means "voice of the river,;. The image needs to look middle eastern or at least evoke something from that side of the world ;-) (we love turqoise, possibly a gate from Morocco or Sephad?), it does not have to be in full focus, but more evocative and ancient. Another idea could be a circular / geometric design . . . . . centered with tiles and artist names above and below.
Updates

The Title of the Album is קול נהר יפי, and underneath that, it should say "Voice of the River, my Fair One". And under that it should say Miriam and Shimon. Old looking fonts, the title of the album could be in an arc, or whatever looks good! THANKS!!!!

Font styles to use
Serif
Decorative
Script

Requirements
Nice to have
• Turquoise, blues

```html
<!DOCTYPE html>
<html lang="en">
<head>
<meta charset="utf-8">
<title>Kol Nahar Yafi – CD Cover</title>
<link href="https://fonts.googleapis.com/css2?family=Stint+Ultra+Condensed&family=Frank+Ruhl+Libre:wght@500&family=IM+Fell+English:ital@0;1&display=swap" rel="stylesheet">
<style>
  :root {
    --paper: #ffffff;
    --title-teal: #11606a;
    --star-stroke: #1a9a98;
    --sand-light: #e8d2b0;
    --sand: #c9a370;
    --sand-dark: #9c7a52;
    --door-turquoise: #2aa7ad;
    --door-deep: #1b7f86;
  }
  html, body {
    margin: 0;
    padding: 0;
    overflow: hidden;
    background: var(--paper);
  }
  .cover {
    position: relative;
    width: 1200px;
    height: 1200px;
    background: var(--paper);
    overflow: hidden;
  }
  .album-title,
  .hebrew-title,
  .subtitle,
  .artists {
    position: absolute;
    left: 0;
    width: 1200px;
    margin: 0;
    text-align: center;
    color: var(--title-teal);
    line-height: 1;
  }
  .album-title {
    top: 34px;
    font-family: "Stint Ultra Condensed", serif;
    font-weight: 400;
    font-size: 120px;
    letter-spacing: 5px;
    text-transform: uppercase;
  }
  .hebrew-title {
    top: 166px;
    font-family: "Frank Ruhl Libre", serif;
    font-weight: 500;
    font-size: 54px;
  }
  .subtitle {
    top: 1068px;
    font-family: "IM Fell English", serif;
    font-style: italic;
    font-size: 50px;
  }
  .artists {
    top: 1134px;
    font-family: "IM Fell English", serif;
    font-size: 40px;
    letter-spacing: 2px;
  }
  .star-frame {
    position: absolute;
    top: 0;
    left: 0;
    width: 1200px;
    height: 1200px;
  }
  .star-outline {
    fill: none;
    stroke: var(--star-stroke);
    stroke-width: 6;
    stroke-linejoin: round;
  }
</style>
</head>
<body>
  <main class="cover">
    <h1 class="album-title">Kol Nahar Yafi</h1>
    <p class="hebrew-title" lang="he" dir="rtl">קול נהר יפי</p>

    <svg class="star-frame" viewBox="0 0 1200 1200" xmlns="http://www.w3.org/2000/svg">
      <defs>
        <radialGradient id="gateGlow" cx="50%" cy="58%" r="55%">
          <stop offset="0%" stop-color="var(--door-turquoise)"/>
          <stop offset="30%" stop-color="var(--door-deep)"/>
          <stop offset="42%" stop-color="var(--sand-light)"/>
          <stop offset="75%" stop-color="var(--sand)"/>
          <stop offset="100%" stop-color="var(--sand-dark)"/>
        </radialGradient>
      </defs>
      <polygon class="star-photo"
               role="img"
               aria-label="Photograph of a weathered turquoise wooden double door set in an arched sandstone gateway, old Mediterranean wall"
               fill="url(#gateGlow)"
               points="591,250 714,444 942,444 838,648 948,845 718,853 603,1050 481,857 250,855 360,655 246,452 476,444"/>
      <polygon class="star-outline"
               points="591,250 714,444 942,444 838,648 948,845 718,853 603,1050 481,857 250,855 360,655 246,452 476,444"/>
    </svg>

    <p class="subtitle">Voice of the River, my Fair One</p>
    <p class="artists">Miriam &amp; Shimon</p>
  </main>
</body>
</html>
```